Business Cards & Stationary for Broadcast Company

We are a satellite company launching a new exciting brand by the name of "Veloran". Veloran is a broadcasting solution provider that gives end-to-end solutions to TV channels and other content providers to deliver and distribute their content globally. Weather it be TV channels that need to be broadcasted in their local regions or internationally, or its collection of news from various locations, or even coverage of special sports or other events, we provide the technology and services to make that happen.
we need a design for business cards as our top priority but also require letterhead and envelope design as well.
Business card will include the following information
Name: Karim Dusoki
Designation: General Manager
Mobile (M): +92 333 4718206
+971 55 2486153 (UAE)
Direct (D): +92 213 6140392
Office (O): +92 213 6142510-14
Fax (F): +92 213 6140392
Email (E): karim@veloran-example.biz
Website: www.veloran-example.biz

```html
<!DOCTYPE html>
<html lang="en">
<head>
<meta charset="utf-8">
<title>Veloran Business Card</title>
<link href="https://fonts.googleapis.com/css2?family=Mulish:wght@400;700&display=swap" rel="stylesheet">
<style>
  :root {
    --stage: #d9d9d6;
    --card-black: #0b0b0b;
    --card-white: #ffffff;
    --ink: #1a1a1a;
    --ink-soft: #3a3a3a;
    --brand-navy: #1b4f9c;
    --brand-blue: #1aa3dc;
    --accent-red: #e31e24;
  }
  * { box-sizing: border-box; margin: 0; padding: 0; }
  html, body {
    width: 1200px; height: 871px; overflow: hidden;
    background: var(--stage);
    font-family: "Mulish", "Century Gothic", sans-serif;
  }
  .canvas { position: relative; width: 1200px; height: 871px; }

  .card {
    position: absolute; width: 700px; height: 400px;
    box-shadow: 0 10px 28px rgba(0,0,0,.28);
    overflow: hidden;
  }

  /* Front */
  .card-front {
    left: 60px; top: 30px;
    background: radial-gradient(circle at 50% 45%, #1a1a1a 0%, var(--card-black) 70%);
  }
  .front-mark {
    position: absolute; left: 0; right: 0; top: 160px;
    display: flex; align-items: center; justify-content: center; gap: 14px;
  }
  .mark-dot {
    width: 22px; height: 22px; border-radius: 50%;
    background: var(--brand-blue);
  }
  .front-name {
    font-weight: 700; font-size: 46px; letter-spacing: 3px;
    color: #9a9a9a; text-transform: uppercase;
  }
  .front-web {
    position: absolute; left: 0; right: 0; top: 300px;
    text-align: center; font-size: 17px; color: #7d7d7d; letter-spacing: .5px;
  }

  /* Back */
  .card-back {
    left: 440px; top: 441px;
    background: linear-gradient(160deg, #ffffff 40%, #ececec 100%);
  }
  .back-mark {
    position: absolute; left: 34px; top: 40px;
    display: flex; align-items: center; gap: 10px;
  }
  .back-mark .mark-dot { width: 16px; height: 16px; }
  .back-name {
    font-weight: 700; font-size: 26px; letter-spacing: 1.5px;
    color: var(--brand-navy); text-transform: uppercase;
  }
  .person {
    position: absolute; left: 400px; top: 120px;
  }
  .person-name { font-weight: 700; font-size: 21px; color: var(--ink); }
  .person-role { font-size: 13px; color: var(--brand-blue); margin-top: 1px; }
  .contacts {
    position: absolute; left: 378px; top: 178px;
    list-style: none;
  }
  .contacts li {
    display: flex; align-items: center; gap: 14px;
    font-size: 14.5px; color: var(--ink-soft); height: 21px;
  }
  .contacts svg { width: 13px; height: 13px; flex: none; }

  .footer-band {
    position: absolute; left: 0; right: 0; bottom: 0; height: 54px;
    background: var(--card-black);
  }
  .footer-rule {
    position: absolute; left: 0; right: 0; bottom: 54px; height: 4px;
    background: var(--brand-blue);
  }
</style>
</head>
<body>
<main class="canvas">

  <section class="card card-front" aria-label="Card front">
    <div class="front-mark">
      <span class="mark-dot"></span>
      <span class="front-name">Veloran</span>
    </div>
    <p class="front-web">www.veloran-example.biz</p>
  </section>

  <section class="card card-back" aria-label="Card back">
    <div class="back-mark">
      <span class="mark-dot"></span>
      <span class="back-name">Veloran</span>
    </div>

    <div class="person">
      <p class="person-name">Karim Dusoki</p>
      <p class="person-role">General Manager</p>
    </div>

    <ul class="contacts">
      <li><svg viewBox="0 0 13 13"><rect x="3" y="1" width="7" height="11" rx="1" fill="none" stroke="#e31e24" stroke-width="1.3"/></svg><span>+92 333 4718206</span></li>
      <li><svg viewBox="0 0 13 13"><rect x="3" y="1" width="7" height="11" rx="1" fill="none" stroke="#e31e24" stroke-width="1.3"/></svg><span>+971 55 2486153 (UAE)</span></li>
      <li><svg viewBox="0 0 13 13"><path d="M2,5 Q6.5,1 11,5 L9.5,6.5 L8,5.5 L5,5.5 L3.5,6.5 Z M3,8 H10 V11.5 H3 Z" fill="#e31e24"/></svg><span>+92 213 6140392</span></li>
      <li><svg viewBox="0 0 13 13"><path d="M2,5 Q6.5,1 11,5 L9.5,6.5 L8,5.5 L5,5.5 L3.5,6.5 Z M3,8 H10 V11.5 H3 Z" fill="#e31e24"/></svg><span>+92 213 6142510-14</span></li>
      <li><svg viewBox="0 0 13 13"><rect x="4" y="1" width="5" height="4" fill="none" stroke="#e31e24" stroke-width="1.2"/><rect x="1.5" y="5" width="10" height="5" fill="#e31e24"/><rect x="4" y="9" width="5" height="3" fill="#fff" stroke="#e31e24" stroke-width="1"/></svg><span>+92 213 6140392</span></li>
      <li><svg viewBox="0 0 13 13"><rect x="1" y="3" width="11" height="8" fill="none" stroke="#e31e24" stroke-width="1.3"/><path d="M1,3 L6.5,8 L12,3" fill="none" stroke="#e31e24" stroke-width="1.3"/></svg><span>karim@veloran-example.biz</span></li>
    </ul>

    <div class="footer-rule"></div>
    <div class="footer-band"></div>
  </section>

</main>
</body>
</html>
```